Rollers & Glides.com

Vertical Business Card with focus on branding with our icon. Information on card will be logo, persons name, position, phone number, email address and website. Use the the name Marcus Tilden, position President, phone number 555.214.8890, email Marcus@rollersandglides.com, website www.rollersandglides.com.

```html
<!DOCTYPE html>
<html lang="en">
<head>
<meta charset="utf-8">
<title>Rollers &amp; Glides – Business Card</title>
<link rel="stylesheet" href="https://fonts.googleapis.com/css2?family=Open+Sans:wght@400;600;700&display=swap">
<style>
  :root {
    --page-bg: #e6ebf2;
    --card-bg: #f3f6fb;
    --brand-blue: #2b4fa3;
    --brand-blue-deep: #1f3f8f;
    --band-text: #e4ebf8;
    --ink-dark: #1b1b1f;
    --ink-light: #ffffff;
    --ink-muted: #d6def0;
  }
  * { box-sizing: border-box; margin: 0; padding: 0; }
  html, body {
    width: 1200px; height: 900px; overflow: hidden;
    background: var(--page-bg);
    font-family: "Open Sans", Arial, sans-serif;
  }
  .card {
    position: absolute; left: 300px; top: 150px;
    width: 600px; height: 600px;
    background: var(--card-bg);
    box-shadow: 0 10px 30px rgba(30, 50, 90, 0.15);
  }
  .tagline-band {
    position: absolute; left: 0; width: 100%; height: 62px;
    background: var(--brand-blue);
    color: var(--band-text);
    display: flex; align-items: center; justify-content: center;
    font-size: 24px; letter-spacing: 2.5px; font-weight: 400;
  }
  .tagline-band strong { font-weight: 600; }
  .tagline-band--top { top: 0; }
  .tagline-band--bottom { bottom: 0; }

  .contact-block {
    position: absolute; left: 50px; top: 110px; width: 500px;
    display: flex; flex-direction: column; gap: 18px;
  }
  .contact-bar {
    display: flex; align-items: center; gap: 16px;
    height: 64px; padding: 0 28px;
    border-radius: 32px;
    background: var(--brand-blue);
    color: var(--ink-light);
  }
  .contact-bar--name { height: 92px; border-radius: 46px; flex-direction: column; align-items: flex-start; justify-content: center; gap: 0; }
  .person-name { font-size: 34px; font-weight: 700; line-height: 1.1; }
  .person-role { font-size: 20px; font-weight: 400; color: var(--ink-muted); }
  .contact-text { font-size: 22px; font-weight: 400; }
  .contact-bar--web { background: var(--ink-dark); }
  .contact-bar--web .contact-text { font-size: 24px; letter-spacing: 0.5px; }
  .contact-icon { width: 26px; height: 26px; flex: none; }

  .brand-signature {
    position: absolute; right: 40px; bottom: 84px;
    display: flex; align-items: center; gap: 12px;
    color: var(--brand-blue-deep);
    font-size: 28px; font-weight: 700;
  }
  .brand-dot {
    width: 22px; height: 22px; border-radius: 50%;
    background: var(--brand-blue-deep);
  }
</style>
</head>
<body>
  <div class="card">
    <div class="tagline-band tagline-band--top"><strong>HIGH-QUALITY</strong>&nbsp;AND INNOVATIVE</div>

    <div class="contact-block">
      <div class="contact-bar contact-bar--name">
        <span class="person-name">Marcus Tilden</span>
        <span class="person-role">President</span>
      </div>

      <div class="contact-bar">
        <svg class="contact-icon" viewBox="0 0 24 24" aria-hidden="true">
          <rect x="2" y="5" width="20" height="14" rx="1.5" fill="none" stroke="#fff" stroke-width="2"/>
          <path d="M3 6l9 7 9-7" fill="none" stroke="#fff" stroke-width="2"/>
        </svg>
        <span class="contact-text">Marcus@rollersandglides.com</span>
      </div>

      <div class="contact-bar">
        <svg class="contact-icon" viewBox="0 0 24 24" aria-hidden="true">
          <path d="M6.6 10.8a15 15 0 0 0 6.6 6.6l2.2-2.2a1 1 0 0 1 1-.25 11.4 11.4 0 0 0 3.6.57 1 1 0 0 1 1 1V20a1 1 0 0 1-1 1A17 17 0 0 1 3 4a1 1 0 0 1 1-1h3.5a1 1 0 0 1 1 1c0 1.25.2 2.45.57 3.57a1 1 0 0 1-.25 1z" fill="#fff"/>
        </svg>
        <span class="contact-text">555.214.8890</span>
      </div>

      <div class="contact-bar contact-bar--web">
        <svg class="contact-icon" viewBox="0 0 24 24" aria-hidden="true">
          <circle cx="12" cy="12" r="9.5" fill="none" stroke="#fff" stroke-width="1.8"/>
          <ellipse cx="12" cy="12" rx="4.2" ry="9.5" fill="none" stroke="#fff" stroke-width="1.5"/>
          <path d="M2.5 12h19M4 7h16M4 17h16" stroke="#fff" stroke-width="1.5"/>
        </svg>
        <span class="contact-text">www.rollersandglides.com</span>
      </div>
    </div>

    <div class="brand-signature">
      <span class="brand-dot"></span>
      <span class="brand-name">Rollers &amp; Glides</span>
    </div>

    <div class="tagline-band tagline-band--bottom"><strong>HIGH-QUALITY</strong>&nbsp;AND INNOVATIVE</div>
  </div>
</body>
</html>
```